Construction Company Business Card

Business Card Design using new Logo

Contact Information for Business Card

include all company info and website

Requirements
Must have
• Marlon Ridgeway - President
ph. 254-716-5093
Oak Hollow, TX
marlon@stonefieldworks.com
www.stonefieldworks.com

```html
<!DOCTYPE html>
<html lang="en">
<head>
<meta charset="utf-8">
<title>Stonefield Works – Business Card</title>
<link href="https://fonts.googleapis.com/css2?family=Montserrat:wght@400;500&family=Arimo:wght@400;700&display=swap" rel="stylesheet">
<style>
  :root {
    --bg: #d9d9d9;
    --ink-black: #111111;
    --ink-black-2: #1e1e1e;
    --paper: #ffffff;
    --red: #c8202b;
    --grey-text: #2b2b2b;
    --light-text: #e4e4e4;
  }
  * { box-sizing: border-box; margin: 0; padding: 0; }
  html, body { width: 1200px; height: 901px; overflow: hidden; background: var(--bg); }
  .canvas { position: relative; width: 1200px; height: 901px; }

  .card {
    position: absolute; left: 260px; width: 680px; height: 388px;
    overflow: hidden; box-shadow: 0 6px 18px rgba(0,0,0,.25);
  }
  .card__band { position: absolute; left: 0; right: 0; bottom: 0; height: 14px; background: var(--red); }

  /* front */
  .card--front { top: 42px; background: linear-gradient(135deg, var(--ink-black-2), var(--ink-black)); }
  .brand {
    display: flex; align-items: center; gap: 12px;
    font-family: "Montserrat", sans-serif; font-weight: 500; letter-spacing: 3px;
    text-transform: uppercase; white-space: nowrap;
  }
  .brand__mark { width: 14px; height: 14px; background: var(--red); }
  .card--front .brand { position: absolute; top: 140px; left: 0; right: 0; justify-content: center; font-size: 34px; color: var(--light-text); }
  .front__url {
    position: absolute; top: 282px; left: 0; right: 0; text-align: center;
    font-family: "Montserrat", sans-serif; font-size: 17px; letter-spacing: 3px; color: var(--light-text);
  }
  .front__url .accent { color: var(--red); }

  /* back */
  .card--back { top: 471px; background: var(--paper); }
  .card--back .brand { position: absolute; top: 172px; left: 40px; font-size: 22px; color: var(--grey-text); gap: 9px; }
  .card--back .brand__mark { width: 10px; height: 10px; }
  .back__rule { position: absolute; left: 370px; top: 95px; width: 2px; height: 178px; background: var(--red); }
  .contact { position: absolute; left: 398px; top: 100px; font-family: "Arimo", sans-serif; color: var(--grey-text); }
  .contact__name { font-size: 29px; font-weight: 700; color: var(--red); line-height: 1; white-space: nowrap; }
  .contact__title { font-size: 17px; margin-top: 3px; }
  .contact__list { list-style: none; margin-top: 26px; }
  .contact__list li { display: flex; align-items: center; gap: 12px; font-size: 15.5px; height: 24px; white-space: nowrap; }
  .contact__list svg { width: 15px; height: 15px; flex: none; stroke: var(--red); fill: none; stroke-width: 1.6; }
</style>
</head>
<body>
<main class="canvas">
  <section class="card card--front">
    <div class="brand"><span class="brand__mark"></span>Stonefield Works</div>
    <p class="front__url">www.<span class="accent">stonefieldworks</span>.com</p>
    <div class="card__band"></div>
  </section>

  <section class="card card--back">
    <div class="brand"><span class="brand__mark"></span>Stonefield Works</div>
    <div class="back__rule"></div>
    <div class="contact">
      <p class="contact__name">Marlon Ridgeway</p>
      <p class="contact__title">President</p>
      <ul class="contact__list">
        <li><svg viewBox="0 0 16 16"><path d="M3 2l3 1 1 3-2 1.5c1 2 2 3 4 4L10.5 9.5l3 1 1 3-2 1.5C7 14 2 9 1.5 3.5z"/></svg>254-716-5093</li>
        <li><svg viewBox="0 0 16 16"><path d="M8 15s5-5 5-8.5A5 5 0 0 0 3 6.5C3 10 8 15 8 15z"/><circle cx="8" cy="6.5" r="1.8"/></svg>Oak Hollow, TX</li>
        <li><svg viewBox="0 0 16 16"><rect x="1.5" y="3.5" width="13" height="9"/><path d="M1.5 3.5L8 9l6.5-5.5"/></svg>marlon@stonefieldworks.com</li>
        <li><svg viewBox="0 0 16 16"><circle cx="8" cy="8" r="6.5"/><ellipse cx="8" cy="8" rx="3" ry="6.5"/><path d="M1.5 8h13"/></svg>www.stonefieldworks.com</li>
      </ul>
    </div>
    <div class="card__band"></div>
  </section>
</main>
</body>
</html>
```